MODERN LAW FIRM BUSINESS CARDS/STATIONERY
Hollister Tax Law
MODERN LAW FIRM BUSINESS CARDS/STATIONERY - Law
Creative Brief
Use same font as used in my logo
Luxury Gold
Simple
DOUGLAS R. HOLLISTER, J.D., LL.M.
Attorney and Counselor
3874 Crandon Avenue Suite 212 Birmingham, MI 48017
doug@hollistertaxcounsel.example
www.hollistertaxcounsel.example
I am open to colors, but want to use the logo. I use Luxury Gold Font for the Hollister Tax Law portion, the rest is up to you. Thanks, Doug
I have offices in the following locations that I would like to highlight: Las Vegas, NV Phoenix, AZ Short Hills, NJ Chicago, IL New York, NY Miami, FL Cleveland, OH Los Angeles, CA Palo Alto, CA San Francisco, CA

```html
<!DOCTYPE html>
<html lang="en">
<head>
<meta charset="utf-8">
<title>Hollister Tax Law Stationery</title>
<link href="https://fonts.googleapis.com/css2?family=Montserrat:wght@400;600&display=swap" rel="stylesheet">
<style>
:root{
  --board:#6f6f6f;
  --paper:#ffffff;
  --ink:#1a1a1a;
  --bar:#111111;
  --gold:#c49a48;
  --navy:#1c2178;
  --rule:#b9b9b9;
  --label:#d8d8d8;
}
*{box-sizing:border-box;margin:0;padding:0}
html,body{width:1200px;height:662px;overflow:hidden}
body{background:var(--board);font-family:'Montserrat',sans-serif;color:var(--ink);position:relative}
.item{position:absolute}
.label{position:absolute;top:-9px;left:0;right:0;text-align:center;font-size:5px;color:var(--label);letter-spacing:.3px;white-space:nowrap}

/* firm name set as plain text */
.firm-name{font-family:'Montserrat',sans-serif;font-weight:600;font-size:8px;letter-spacing:.6px;line-height:1;white-space:nowrap}
.firm-name.gold{color:var(--gold)}
.firm-name.black{color:var(--ink)}
.firm-name.navy{color:var(--navy)}
.firm-name.white{color:#fff}

/* letterhead */
.sheet{background:var(--paper);box-shadow:0 1px 3px rgba(0,0,0,.35)}
.sheet .side-bar{position:absolute;left:8px;top:0;bottom:0;width:11px;background:var(--bar)}
.sheet .firm-name{position:absolute;left:26px;top:12px}
.form{position:absolute;left:26px;top:44px;width:110px;font-size:4.5px;color:#555}
.form .row{display:flex;gap:8px;border-bottom:.5px solid var(--rule);padding:2px 0}
.form .row span{flex:1}
.checks{position:absolute;left:26px;top:86px;display:flex;gap:9px;font-size:4.5px;color:#555}
.checks span::before{content:"";display:inline-block;width:4px;height:4px;border:.5px solid #777;margin-right:2px;vertical-align:-.5px}
.footer{position:absolute;left:26px;right:8px;bottom:6px;font-size:4px;color:#666;text-align:center;letter-spacing:.2px}

/* cards */
.card{width:96px;height:52px;box-shadow:0 1px 2px rgba(0,0,0,.4);display:flex;align-items:center;justify-content:center;position:absolute;overflow:hidden}
.card.white{background:var(--paper)}
.card.gold{background:linear-gradient(135deg,#b8893a,#e2c07a 50%,#a77c32)}
.card.black{background:#0d0d0d}
.card.navy{background:var(--navy)}
.card .firm-name{font-size:5.5px;letter-spacing:.4px}
.card.back{flex-direction:column;align-items:flex-start;justify-content:center;padding-left:7px;font-size:3.3px;line-height:1.5;color:#333;white-space:nowrap}
.card.back.dark{color:#eee}
.card.back .who{font-weight:600;font-size:3.6px}
.card .edge{position:absolute;left:0;top:0;bottom:0;width:5px}

/* notecards */
.note{width:236px;height:106px;background:var(--paper);box-shadow:0 1px 3px rgba(0,0,0,.35);position:absolute;left:936px}
.note .side-bar{position:absolute;left:8px;top:0;bottom:0;width:9px;background:var(--bar)}
.note .firm-name{position:absolute;left:50%;top:16px;transform:translateX(-50%)}

/* envelopes */
.envelope{position:absolute;left:936px;width:236px;height:70px}
.envelope svg{display:block}
.envelope .firm-name{position:absolute;left:50%;top:26px;transform:translateX(-50%);font-size:6px}
.envelope .addr{position:absolute;left:0;right:0;bottom:6px;text-align:center;font-size:3.8px;color:#444}
</style>
</head>
<body>

<div class="item sheet" style="left:24px;top:19px;width:210px;height:290px">
  <div class="label">Letterhead Gold</div>
  <div class="side-bar"></div>
  <div class="firm-name gold">HOLLISTER TAX LAW</div>
  <div class="form">
    <div class="row"><span>To:</span><span>Fax:</span></div>
    <div class="row"><span>From:</span><span>Pages:</span></div>
    <div class="row"><span>Date:</span><span>Re:</span></div>
  </div>
  <div class="checks"><span>Urgent</span><span>Review</span><span>Reply</span><span>Recycle</span><span>Note</span></div>
  <div class="footer">3874 Crandon Avenue Suite 212 Birmingham, MI 48017 · www.hollistertaxcounsel.example</div>
</div>

<div class="item sheet" style="left:242px;top:19px;width:221px;height:290px">
  <div class="label">Second Page</div>
  <div class="side-bar"></div>
  <div class="firm-name gold">HOLLISTER TAX LAW</div>
</div>

<div class="item sheet" style="left:24px;top:338px;width:210px;height:310px">
  <div class="label">Letterhead Black</div>
  <div class="side-bar"></div>
  <div class="firm-name black">HOLLISTER TAX LAW</div>
  <div class="form">
    <div class="row"><span>To:</span><span>Fax:</span></div>
    <div class="row"><span>From:</span><span>Pages:</span></div>
    <div class="row"><span>Date:</span><span>Re:</span></div>
  </div>
  <div class="checks"><span>Urgent</span><span>Review</span><span>Reply</span><span>Recycle</span><span>Note</span></div>
  <div class="footer">3874 Crandon Avenue Suite 212 Birmingham, MI 48017 · www.hollistertaxcounsel.example</div>
</div>

<div class="item sheet" style="left:242px;top:338px;width:221px;height:310px">
  <div class="label">Second Page</div>
  <div class="side-bar"></div>
  <div class="firm-name black">HOLLISTER TAX LAW</div>
</div>

<div class="item sheet" style="left:475px;top:338px;width:221px;height:310px">
  <div class="label">Letterhead Navy</div>
  <div class="side-bar"></div>
  <div class="firm-name navy">HOLLISTER TAX LAW</div>
  <div class="form">
    <div class="row"><span>To:</span><span>Fax:</span></div>
    <div class="row"><span>From:</span><span>Pages:</span></div>
    <div class="row"><span>Date:</span><span>Re:</span></div>
  </div>
  <div class="checks"><span>Urgent</span><span>Review</span><span>Reply</span><span>Recycle</span><span>Note</span></div>
  <div class="footer">3874 Crandon Avenue Suite 212 Birmingham, MI 48017 · www.hollistertaxcounsel.example</div>
</div>

<div class="item sheet" style="left:705px;top:338px;width:214px;height:310px">
  <div class="label">Second Page</div>
  <div class="footer">www.hollistertaxcounsel.example</div>
</div>

<div class="item" style="left:475px;top:115px;width:425px">
  <div class="label">Card Set Gold</div>
  <div class="card white" style="left:0;top:0"><span class="edge" style="background:var(--bar)"></span><span class="firm-name gold">HOLLISTER TAX LAW</span></div>
  <div class="card gold" style="left:110px;top:0"><span class="firm-name white">HOLLISTER TAX LAW</span></div>
  <div class="card black" style="left:220px;top:0"><span class="firm-name gold">HOLLISTER TAX LAW</span></div>
  <div class="card white back" style="left:329px;top:0">
    <span class="who">DOUGLAS R. HOLLISTER, J.D., LL.M.</span><span>Attorney and Counselor</span><span>3874 Crandon Avenue Suite 212</span><span>Birmingham, MI 48017</span><span>doug@hollistertaxcounsel.example</span>
  </div>
</div>

<div class="item" style="left:475px;top:190px;width:425px">
  <div class="label">Card Set Black</div>
  <div class="card white" style="left:0;top:0"><span class="edge" style="background:var(--bar)"></span><span class="firm-name black">HOLLISTER TAX LAW</span></div>
  <div class="card white back" style="left:110px;top:0">
    <span class="who">DOUGLAS R. HOLLISTER, J.D., LL.M.</span><span>Attorney and Counselor</span><span>3874 Crandon Avenue Suite 212</span><span>Birmingham, MI 48017</span><span>www.hollistertaxcounsel.example</span>
  </div>
  <div class="card black" style="left:220px;top:0"><span class="firm-name white">HOLLISTER TAX LAW</span></div>
  <div class="card black back dark" style="left:329px;top:0">
    <span class="who">DOUGLAS R. HOLLISTER, J.D., LL.M.</span><span>Attorney and Counselor</span><span>3874 Crandon Avenue Suite 212</span><span>Birmingham, MI 48017</span><span>doug@hollistertaxcounsel.example</span>
  </div>
</div>

<div class="item" style="left:475px;top:265px;width:425px">
  <div class="label">Card Set Navy</div>
  <div class="card white" style="left:0;top:0"><span class="edge" style="background:var(--bar)"></span><span class="firm-name navy">HOLLISTER TAX LAW</span></div>
  <div class="card white back" style="left:110px;top:0">
    <span class="who">DOUGLAS R. HOLLISTER, J.D., LL.M.</span><span>Attorney and Counselor</span><span>3874 Crandon Avenue Suite 212</span><span>Birmingham, MI 48017</span><span>www.hollistertaxcounsel.example</span>
  </div>
  <div class="card navy" style="left:220px;top:0"><span class="firm-name white">HOLLISTER TAX LAW</span></div>
  <div class="card white back" style="left:329px;top:0">
    <span class="who">DOUGLAS R. HOLLISTER, J.D., LL.M.</span><span>Attorney and Counselor</span><span>3874 Crandon Avenue Suite 212</span><span>Birmingham, MI 48017</span><span>doug@hollistertaxcounsel.example</span>
  </div>
</div>

<div class="note" style="top:19px"><div class="label">Notecard Gold</div><div class="side-bar"></div><div class="firm-name gold">HOLLISTER TAX LAW</div></div>
<div class="note" style="top:147px"><div class="label">Notecard Black</div><div class="side-bar"></div><div class="firm-name black">HOLLISTER TAX LAW</div></div>
<div class="note" style="top:275px"><div class="label">Notecard Navy</div><div class="side-bar"></div><div class="firm-name navy">HOLLISTER TAX LAW</div></div>

<div class="envelope" style="top:410px">
  <div class="label">Envelope Set</div>
  <svg width="236" height="70" viewBox="0 0 236 70"><rect width="236" height="70" fill="#fff"/><path d="M0 0 L118 44 L236 0 Z" fill="#f2f2f2" stroke="#ccc" stroke-width=".6"/></svg>
  <div class="firm-name gold">HOLLISTER TAX LAW</div>
  <div class="addr">3874 Crandon Avenue Suite 212 Birmingham, MI 48017</div>
</div>
<div class="envelope" style="top:486px">
  <svg width="236" height="70" viewBox="0 0 236 70"><rect width="236" height="70" fill="#fff"/><path d="M0 0 L118 44 L236 0 Z" fill="#0d0d0d"/></svg>
  <div class="firm-name white">HOLLISTER TAX LAW</div>
  <div class="addr">3874 Crandon Avenue Suite 212 Birmingham, MI 48017</div>
</div>
<div class="envelope" style="top:562px">
  <svg width="236" height="70" viewBox="0 0 236 70"><rect width="236" height="70" fill="#fff"/><path d="M0 0 L118 44 L236 0 Z" fill="#1c2178"/></svg>
  <div class="firm-name white">HOLLISTER TAX LAW</div>
  <div class="addr">3874 Crandon Avenue Suite 212 Birmingham, MI 48017</div>
</div>

</body>
</html>
```